Building Design company needing a letterhead

We need a letter head for our Building Design company to send letters etc. to our clients, consultants, councils etc. We would like to see our logo used and company colours. I have attached our style guide and an example of our current letterheads. Top left we would like our logo, top right we would like the company details and at the footer we would like some sort of image/design etc. that suits our brand. I like the Quarto Design letterhead attached.

Target Market(s)

Professionals, Councils, Consultants, Mums & Dads

Industry/Entity Type

Architecture

Font styles to use
Other font styles liked:
• refer the design style guide

Colors
f37122
000000
1b1b1b

Requirements
Must have
• Must have the minimum of a logo, company details and footer
Nice to have
• An image/design made for the footer that would suite our brand and website at www.tavorendesign.com.au. Also it would be nice to include the KMOTR logo somewhere perhaps included in the footer.
Should not have
• Large images in the header. I just want the logo and company details.

```html
<!DOCTYPE html>
<html lang="en">
<head>
<meta charset="utf-8">
<title>Tavoren Design – Letterhead</title>
<link href="https://fonts.googleapis.com/css2?family=Exo+2:wght@600&family=Questrial&display=swap" rel="stylesheet">
<style>
  :root {
    --brand-orange: #e55a27;
    --ink: #1b1b1b;
    --rule: #d9d9d9;
    --paper: #ffffff;
    --faint-grey: #ececec;
    --faint-orange: #fbece7;
  }
  * { margin: 0; padding: 0; box-sizing: border-box; }
  html, body { width: 847px; height: 1200px; overflow: hidden; background: var(--paper); }
  .letterhead {
    position: relative;
    width: 847px;
    height: 1200px;
    background: var(--paper);
    font-family: "Questrial", sans-serif;
    color: var(--ink);
  }
  .masthead {
    position: absolute;
    left: 0; top: 0;
    width: 100%;
    height: 122px;
    border-bottom: 1px solid var(--rule);
  }
  .brand {
    position: absolute;
    left: 24px; top: 34px;
    display: flex;
    align-items: center;
    gap: 12px;
  }
  .brand-square {
    width: 40px; height: 40px;
    background: var(--brand-orange);
  }
  .brand-name {
    font-family: "Exo 2", sans-serif;
    font-weight: 600;
    font-size: 29px;
    line-height: 30px;
    letter-spacing: 1px;
    color: var(--ink);
    text-transform: uppercase;
  }
  .contact {
    position: absolute;
    right: 28px; top: 20px;
    text-align: right;
    font-variant: small-caps;
    text-transform: lowercase;
    letter-spacing: 2px;
  }
  .contact-name {
    color: var(--brand-orange);
    font-size: 15px;
    line-height: 17px;
    margin-right: 12px;
  }
  .contact-role {
    font-size: 13px;
    line-height: 15px;
    margin-right: 12px;
    margin-bottom: 10px;
  }
  .contact-line {
    display: flex;
    justify-content: flex-end;
    align-items: center;
    gap: 8px;
    font-size: 13px;
    line-height: 19px;
  }
  .contact-line svg { width: 10px; height: 10px; flex: none; }
  .backdrop-mark {
    position: absolute;
    left: 0; top: 300px;
    width: 100%;
    text-align: center;
    font-family: "Exo 2", sans-serif;
    font-weight: 600;
    font-size: 150px;
    line-height: 1;
    letter-spacing: 4px;
    color: var(--faint-orange);
    text-transform: uppercase;
  }
  .footer-rule {
    position: absolute;
    left: 0; top: 1126px;
    width: 100%;
    border-top: 1px solid var(--rule);
  }
  .footer-band {
    position: absolute;
    left: 0; bottom: 0;
    width: 100%;
    height: 66px;
    background: var(--brand-orange);
    color: var(--paper);
    text-align: center;
    font-variant: small-caps;
    letter-spacing: 2px;
    font-size: 13px;
    line-height: 20px;
    padding-top: 12px;
  }
</style>
</head>
<body>
<div class="letterhead">
  <header class="masthead">
    <div class="brand">
      <div class="brand-square"></div>
      <div class="brand-name">Tavoren<br>Design</div>
    </div>
    <div class="contact">
      <div class="contact-name">Alex Morgan</div>
      <div class="contact-role">Deisgnation</div>
      <div class="contact-line">(123) 456-7890
        <svg viewBox="0 0 10 10"><path d="M2 1 L4 1 L4.5 3 L3.3 3.8 Q4.2 6 6.2 6.8 L7 5.5 L9 6 L9 8 Q8.5 9 7.5 9 Q1 8 1 2 Q1 1 2 1 Z" fill="var(--brand-orange)"/></svg>
      </div>
      <div class="contact-line">info@companyname.com
        <svg viewBox="0 0 10 10"><rect x="0.5" y="2" width="9" height="6.5" fill="var(--brand-orange)"/><path d="M0.5 2 L5 5.8 L9.5 2" stroke="#fff" stroke-width="0.8" fill="none"/></svg>
      </div>
      <div class="contact-line">companyname.com
        <svg viewBox="0 0 10 10" fill="none" stroke="var(--brand-orange)" stroke-width="0.8"><circle cx="5" cy="5" r="4.3"/><ellipse cx="5" cy="5" rx="1.9" ry="4.3"/><path d="M0.7 5 H9.3 M1.5 2.8 H8.5 M1.5 7.2 H8.5"/></svg>
      </div>
    </div>
  </header>

  <div class="backdrop-mark" aria-hidden="true">Tavoren</div>

  <div class="footer-rule"></div>
  <footer class="footer-band">
    <div>Address line1, address line2</div>
    <div>country - 123456</div>
  </footer>
</div>
</body>
</html>
```